Prickly Heat Powder

prickly heat powders are used in summers to provide cooling effect to body and relief body from heat effects during summers.

we have 4 variants of prickly heat.

1) Menthol
2) Rose
3) Lemon
4) Neem

Bottle is in round cylinder shape. It also has a cap. Will share pictures of bottle and cap tomorrow.

Brand Name is KAVELO.

Total label size will be 180mm width * 140mm height. But main design will be small because bottle is round.

Target Market(s)

B Class.
C plus and C.
Masses

Industry/Entity Type

Cosmetics

Requirements
Must have
• icy effect, joyful and playful
Nice to have
• joyful and eye catching designs. more colors would be good.
• Polar bear might look nice.
• Kavelo Logo to be bold and prominent.

```html
<!DOCTYPE html>
<html lang="en">
<head>
<meta charset="utf-8">
<title>Kavelo Prickly Heat Powder – Label Range</title>
<link rel="stylesheet" href="https://fonts.googleapis.com/css2?family=Arimo:wght@400;700&display=swap">
<style>
  :root {
    --page-bg: #ffffff;
    --label-bg: #f7f8f8;
    --label-edge: #e3e6e6;
    --brand-brown: #3a1e12;
    --ink: #1d1d1d;
    --rose: #f2a6ae;
    --menthol: #9fe3b0;
    --lemon: #f7ea6a;
    --neem: #9cc3f0;
  }
  * { box-sizing: border-box; margin: 0; padding: 0; }
  html, body {
    width: 1200px; height: 900px; overflow: hidden;
    background: var(--page-bg);
    font-family: "Arimo", Arial, sans-serif;
  }
  .range {
    width: 1200px; height: 900px;
    display: flex; justify-content: center; align-items: center; gap: 44px;
  }
  .label {
    position: relative;
    width: 236px; height: 620px;
    background: var(--label-bg);
    border: 1px solid var(--label-edge);
    border-radius: 6px;
    overflow: hidden;
    display: flex; flex-direction: column; align-items: center;
  }
  .label__wash {
    position: absolute; left: 0; right: 0; top: 250px; bottom: 0;
  }
  .label--rose .label__wash { background: linear-gradient(160deg, rgba(255,255,255,0) 0%, var(--rose) 45%, #fbe3e6 80%, #fff 100%); }
  .label--menthol .label__wash { background: linear-gradient(160deg, rgba(255,255,255,0) 0%, var(--menthol) 45%, #def6e4 80%, #fff 100%); }
  .label--lemon .label__wash { background: linear-gradient(160deg, rgba(255,255,255,0) 0%, var(--lemon) 45%, #fbf5c2 80%, #fff 100%); }
  .label--neem .label__wash { background: linear-gradient(160deg, rgba(255,255,255,0) 0%, var(--neem) 45%, #dcebfa 80%, #fff 100%); }
  .brand {
    position: relative;
    margin-top: 120px;
    font-size: 50px; font-weight: 700;
    color: var(--brand-brown);
    letter-spacing: 0.5px;
  }
  .product {
    position: relative;
    margin-top: 60px;
    text-align: center; color: var(--ink);
  }
  .product__kind { font-size: 19px; letter-spacing: 1.5px; }
  .product__type { font-size: 30px; letter-spacing: 3px; margin-top: 8px; }
  .variant {
    position: absolute; bottom: 60px; left: 0; right: 0;
    text-align: center; font-size: 16px; color: var(--ink);
  }
</style>
</head>
<body>
<main class="range">
  <section class="label label--rose">
    <div class="label__wash" role="img" aria-label="Soft pink faceted crystal pattern"></div>
    <div class="brand">Kavelo</div>
    <div class="product"><div class="product__kind">PRICKLY HEAT</div><div class="product__type">POWDER</div></div>
    <div class="variant">Rose</div>
  </section>
  <section class="label label--menthol">
    <div class="label__wash" role="img" aria-label="Soft mint green faceted crystal pattern"></div>
    <div class="brand">Kavelo</div>
    <div class="product"><div class="product__kind">PRICKLY HEAT</div><div class="product__type">POWDER</div></div>
    <div class="variant">Menthol</div>
  </section>
  <section class="label label--lemon">
    <div class="label__wash" role="img" aria-label="Soft yellow faceted crystal pattern"></div>
    <div class="brand">Kavelo</div>
    <div class="product"><div class="product__kind">PRICKLY HEAT</div><div class="product__type">POWDER</div></div>
    <div class="variant">Lemon</div>
  </section>
  <section class="label label--neem">
    <div class="label__wash" role="img" aria-label="Soft blue faceted crystal pattern"></div>
    <div class="brand">Kavelo</div>
    <div class="product"><div class="product__kind">PRICKLY HEAT</div><div class="product__type">POWDER</div></div>
    <div class="variant">Neem</div>
  </section>
</main>
</body>
</html>
```